Bar and Grill looking or a Responsive Web design

New Bar and Grill in the Toronto area just opened up and is looking for a new wordpress website to start off his business.

Their business revolves around a homey family, upbeat atmosphere. His cuisine is gourmet pub style food. Speciality are home made burgers. 90 Seat restaurant in a very diverse and high density neighbourhood.

Looking for a responsive web design that will focus on a key feature pages.

Homepage
- Navigation is easy and simple, emphasize easy navigation in Mobile view.
- Contact information is a click or touch away

About Page

Menu Page
-Menu styling to be responsive. Very simple navigation through different menus and then menu would appear.

Gallery

Contact page
- Map (not trevlosk)
- Contact Details
- Contact/Feedback form

They do have a logo and will be uploaded.

We are open to any designs, as well as designs based off templates that have already been created.

Target Market(s)

Target audience is the varied. They are in an area that's densely populated and very diverse. Looking for a crowd that appreciates a setting for sports, good gourmet pub styled food and a home styled restaurant.

Industry/Entity Type

Restaurant

Colors

Designer to choose colors to be used in the design.

Requirements
Must have
• Menus have to have responsive design for both mobile and tablet/desktop.
Nice to have
• Easy access contact button on mobile view. That way it will act like a webapp so that mobile devices can take advantage of quick touches to get in contact.

```html
<!DOCTYPE html>
<html lang="en">
<head>
<meta charset="utf-8">
<title>Maplecroft Bar &amp; Grill</title>
<link href="https://fonts.googleapis.com/css2?family=Open+Sans:wght@400;600&family=Italianno&display=swap" rel="stylesheet">
<style>
:root{
  --ink:#2b2b2b;
  --header:#262626;
  --nav-line:#3a3a3a;
  --accent:#d2401f;
  --accent-soft:#c2572c;
  --script:#c0683a;
  --paper:#f2f1ee;
  --card:#ffffff;
  --muted:#8a8a8a;
  --footer:#c1703a;
  --gold:#e5b54a;
}
*{margin:0;padding:0;box-sizing:border-box}
html,body{width:802px;height:1200px;overflow:hidden}
body{font-family:"Open Sans",Arial,sans-serif;background:var(--paper);color:var(--ink);position:relative}
.site-header{position:absolute;left:0;top:0;width:802px;height:135px;background:var(--header)}
.brand{position:absolute;top:30px;left:0;width:802px;text-align:center;display:flex;justify-content:center;align-items:center;gap:8px}
.brand-dot{width:10px;height:10px;border-radius:50%;background:var(--accent)}
.brand-name{font-family:"Open Sans",Arial,sans-serif;font-weight:600;font-size:20px;color:var(--gold);letter-spacing:1px}
.main-nav{position:absolute;top:98px;left:0;width:802px;height:37px;border-top:1px solid var(--nav-line);display:flex;justify-content:center;align-items:center;gap:21px}
.main-nav a{color:#d9d9d9;text-decoration:none;font-size:7.5px;letter-spacing:1.4px}
.hero{position:absolute;left:0;top:135px;width:802px;height:246px;background:radial-gradient(ellipse at 60% 45%,#c0392b 0%,#8e4a22 35%,#5a3a22 65%,#2c2118 100%)}
.hero-panel{position:absolute;left:51px;top:0;width:227px;height:246px;background:rgba(40,40,40,.72);padding:32px 23px 0 23px}
.script-title{font-family:"Italianno",cursive;font-weight:400}
.hero-panel h1{font-size:36px;line-height:28px;color:var(--gold)}
.hero-panel p{margin-top:14px;font-size:6.8px;line-height:12.2px;color:#e0e0e0}
.btn{display:inline-block;background:var(--accent);color:#fff;font-size:7.5px;padding:3px 8px;text-decoration:none}
.hero-panel .btn{margin-top:10px}
.hero-dots{position:absolute;left:384px;top:230px;display:flex;gap:6px}
.hero-dots span{width:5px;height:5px;border-radius:50%;background:rgba(255,255,255,.5)}
.to-top{position:absolute;left:770px;top:184px;width:26px;height:26px;border-radius:50%;background:#fff;display:flex;align-items:center;justify-content:center}
.section-head{position:absolute;left:0;width:802px;text-align:center}
.section-head h2{font-size:38px;color:var(--script);line-height:34px}
.section-head p{font-size:7px;color:var(--muted)}
.welcome{position:absolute;left:0;top:381px;width:802px;height:202px}
.feature{position:absolute;top:70px;width:222px;height:100px;background:var(--paper);border:1px solid #e2e0dc;border-bottom:2px solid var(--accent);padding:16px 12px 0 60px}
.feature svg{position:absolute;left:16px;top:16px}
.feature h3{font-size:13.5px;font-weight:600;color:#333}
.feature p{margin-top:4px;font-size:6.8px;line-height:11.4px;color:var(--muted)}
.favorites{position:absolute;left:0;top:583px;width:802px;height:313px;background:radial-gradient(ellipse at 20% 10%,#f3d9a3 0%,#e2a75a 40%,#b86d2e 80%,#9b5a28 100%)}
.favorites .section-head p{color:#9a7a5a}
.dish{position:absolute;top:71px;width:162px;height:211px;background:var(--card)}
.dish-photo{height:106px}
.dish h4{margin:10px 0 0 12px;font-size:9.5px;font-weight:400;color:var(--accent-soft)}
.dish p{margin:5px 12px 0;font-size:6.8px;line-height:11.4px;color:var(--muted)}
.dish .btn{margin:4px 0 0 12px;padding:3px 12px}
.updates{position:absolute;left:0;top:896px;width:802px;height:260px}
.col-head{position:absolute;top:20px;text-align:center}
.col-head h2{font-size:34px;color:var(--script);line-height:30px}
.col-head p{font-size:7px;color:var(--muted)}
.news-item{position:absolute;left:51px;width:345px;height:44px}
.date{position:absolute;left:0;top:3px;width:36px;height:36px;border:1px solid #e2e0dc;background:#fff;text-align:center}
.date b{display:block;font-weight:400;font-size:13px;color:var(--accent);line-height:24px}
.date i{display:block;font-style:normal;font-size:5.5px;background:var(--accent);color:#fff;line-height:11px}
.news-item h5,.menu-item h5{font-size:10px;font-weight:600;color:#333}
.news-item h5{margin-left:47px}
.news-item p{margin:4px 0 0 47px;font-size:6.6px;line-height:10.6px;color:var(--muted)}
.news-item p a,.text-link{color:var(--accent-soft);text-decoration:none}
.menu-item{position:absolute;left:411px;width:341px;height:70px}
.menu-photo{position:absolute;left:0;top:0;width:102px;height:68px;border:3px solid #fff;box-shadow:0 0 0 1px #ddd}
.menu-item h5{margin-left:111px}
.menu-item p{margin:4px 0 0 111px;font-size:6.6px;line-height:10.6px;color:var(--muted)}
.site-footer{position:absolute;left:0;top:1156px;width:802px;height:44px;background:var(--footer);display:flex;justify-content:space-between;align-items:center;padding:0 51px;font-size:6.8px;color:#fff}
.footer-links{display:flex;gap:9px}
.footer-links a{color:#fff;text-decoration:none}
</style>
</head>
<body>
<header class="site-header">
  <div class="brand"><span class="brand-dot"></span><span class="brand-name">MAPLECROFT BAR &amp; GRILL</span></div>
  <nav class="main-nav">
    <a href="#">HOME</a><a href="#">ABOUT US</a><a href="#">MENUS</a><a href="#">GALLERY</a><a href="#">CONTACT</a>
  </nav>
</header>

<section class="hero" role="img" aria-label="Close-up of a pizza topped with tomatoes, olives and rocket on a wooden board">
  <div class="hero-panel">
    <h1 class="script-title">Fresh &amp;<br>Delicious</h1>
    <p>Lorem ipsum dolor sit amet, consectetur adipisicing elit, sed do eiusmod tempor incididunt ut labore et dolore magna aliqua. Ut enim ad minim veniam, quis nostrud exercitation ullamco laboris nisi ut aliquip ex ea commodo consequat. Duis aute irure dolor in reprehenderit in voluptate velit esse cillum dolore eu fugiat nulla pariatur.</p>
    <a class="btn" href="#">Read More</a>
  </div>
  <div class="hero-dots"><span></span><span></span><span></span></div>
  <div class="to-top"><svg width="12" height="8" viewBox="0 0 12 8"><path d="M0 8 L6 1 L12 8Z" fill="#333"/></svg></div>
</section>

<section class="welcome">
  <div class="section-head" style="top:22px">
    <h2 class="script-title">Welcome!</h2>
    <p>Lorem ipsum dolor sit amet, consectetur adipisicing elit</p>
  </div>
  <div class="feature" style="left:51px">
    <svg width="24" height="26" viewBox="0 0 24 26"><path d="M2 0H22V26L12 18L2 26Z" fill="var(--accent)"/></svg>
    <h3>Find Your Favorite</h3>
    <p>Lorem ipsum dolor sit amet, consectetur adipisicing elit, sed do eiusmod tempor incididunt ut labore et dolore magna aliqua.</p>
  </div>
  <div class="feature" style="left:290px">
    <svg width="28" height="26" viewBox="0 0 28 26"><path d="M14 0L17.3 9.5H27.5L19.3 15.5L22.4 25.5L14 19.5L5.6 25.5L8.7 15.5L0.5 9.5H10.7Z" fill="var(--accent)"/></svg>
    <h3>Best Seller</h3>
    <p>Lorem ipsum dolor sit amet, consectetur adipisicing elit, sed do eiusmod tempor incididunt ut labore et dolore magna aliqua.</p>
  </div>
  <div class="feature" style="left:530px">
    <svg width="28" height="27" viewBox="0 0 28 27"><rect x="1" y="4" width="26" height="22" fill="none" stroke="var(--accent)" stroke-width="2"/><rect x="1" y="4" width="26" height="6" fill="var(--accent)"/><rect x="7" y="0" width="2" height="6" fill="var(--accent)"/><rect x="19" y="0" width="2" height="6" fill="var(--accent)"/><g fill="var(--accent)"><rect x="5" y="13" width="4" height="3"/><rect x="12" y="13" width="4" height="3"/><rect x="19" y="13" width="4" height="3"/><rect x="5" y="19" width="4" height="3"/><rect x="12" y="19" width="4" height="3"/><rect x="19" y="19" width="4" height="3"/></g></svg>
    <h3>Choose Best</h3>
    <p>Lorem ipsum dolor sit amet, consectetur adipisicing elit, sed do eiusmod tempor incididunt ut labore et dolore magna aliqua.</p>
  </div>
</section>

<section class="favorites" role="img" aria-label="Soft warm blurred background of grilled food">
  <div class="section-head" style="top:24px">
    <h2 class="script-title">Favorite Menu</h2>
    <p>Lorem ipsum dolor sit amet, consectetur adipisicing elit</p>
  </div>
  <article class="dish" style="left:51px">
    <div class="dish-photo" role="img" aria-label="Grilled steak with rosemary" style="background:linear-gradient(160deg,#4a3a2c,#8a4a34 55%,#5a4636)"></div>
    <h4>Neque porro quisquam</h4>
    <p>Lorem ipsum dolor sit amet, consectetur adipisicing elit, sed do eiusmod tempor incididunt ut labore et dolore magna</p>
    <a class="btn" href="#">More</a>
  </article>
  <article class="dish" style="left:230px">
    <div class="dish-photo" role="img" aria-label="Greek salad with olives, cucumber and tomatoes" style="background:linear-gradient(160deg,#7a3a2a,#5d8a3a 50%,#e8e8e0)"></div>
    <h4>Neque porro quisquam</h4>
    <p>Lorem ipsum dolor sit amet, consectetur adipisicing elit, sed do eiusmod tempor incididunt ut labore et dolore magna</p>
    <a class="btn" href="#">More</a>
  </article>
  <article class="dish" style="left:411px">
    <div class="dish-photo" role="img" aria-label="Roast chicken pieces with herbs" style="background:linear-gradient(160deg,#3a2a1e,#b8702e 50%,#6a4024)"></div>
    <h4>Neque porro quisquam</h4>
    <p>Lorem ipsum dolor sit amet, consectetur adipisicing elit, sed do eiusmod tempor incididunt ut labore et dolore magna</p>
    <a class="btn" href="#">More</a>
  </article>
  <article class="dish" style="left:590px">
    <div class="dish-photo" role="img" aria-label="Curry with peppers in a metal pan" style="background:linear-gradient(160deg,#d8d0c4,#9a3a1e 50%,#5a3424)"></div>
    <h4>Neque porro quisquam</h4>
    <p>Lorem ipsum dolor sit amet, consectetur adipisicing elit, sed do eiusmod tempor incididunt ut labore et dolore magna</p>
    <a class="btn" href="#">More</a>
  </article>
</section>

<section class="updates">
  <div class="col-head" style="left:51px;width:340px">
    <h2 class="script-title">Latest News</h2>
    <p>Lorem ipsum dolor sit amet, consectetur adipisicing elit</p>
  </div>
  <div class="col-head" style="left:411px;width:341px">
    <h2 class="script-title">New Menu</h2>
    <p>Lorem ipsum dolor sit amet, consectetur adipisicing elit</p>
  </div>

  <article class="news-item" style="top:70px">
    <div class="date"><b>28</b><i>SEP</i></div>
    <h5>Lorem ipsum sit amet</h5>
    <p>Nemo enim ipsam voluptatem quia voluptas sit aspernatur aut odit aut fugit, sed quia consequuntur magni dolores eos qui ratione voluptatem. <a href="#">Read more</a></p>
  </article>
  <article class="news-item" style="top:120px">
    <div class="date"><b>26</b><i>SEP</i></div>
    <h5>Lorem ipsum sit amet</h5>
    <p>Nemo enim ipsam voluptatem quia voluptas sit aspernatur aut odit aut fugit, sed quia consequuntur magni dolores eos qui ratione voluptatem. <a href="#">Read more</a></p>
  </article>
  <article class="news-item" style="top:170px">
    <div class="date"><b>18</b><i>SEP</i></div>
    <h5>Lorem ipsum sit amet</h5>
    <p>Nemo enim ipsam voluptatem quia voluptas sit aspernatur aut odit aut fugit, sed quia consequuntur magni dolores eos qui ratione voluptatem. <a href="#">Read more</a></p>
  </article>

  <article class="menu-item" style="top:74px">
    <div class="menu-photo" role="img" aria-label="Plated ribs with fries and vegetables" style="background:linear-gradient(160deg,#c8b8a0,#5a3020 55%,#e0dcd4)"></div>
    <h5>Neque porro quisquam</h5>
    <p>Lorem ipsum dolor sit amet, consectetur adipisicing elit, sed do eiusmod tempor incididunt ut labore et dolore magna aliqua. Ut enim ad minim veniam, quis nostrud exercitation ullamco laboris nisi ut aliquip ex ea commodo consequat.</p>
  </article>
  <article class="menu-item" style="top:152px">
    <div class="menu-photo" role="img" aria-label="Grilled meat on a wooden board" style="background:linear-gradient(160deg,#4a2a1c,#a0522d 55%,#3a2418)"></div>
    <h5>Neque porro quisquam</h5>
    <p>Lorem ipsum dolor sit amet, consectetur adipisicing elit, sed do eiusmod tempor incididunt ut labore et dolore magna aliqua. Ut enim ad minim veniam, quis nostrud exercitation ullamco laboris nisi ut aliquip ex ea commodo consequat.</p>
  </article>
</section>

<footer class="site-footer">
  <span>© Copyright 2013 - 14 - Maplecroft Bar &amp; Grill</span>
  <nav class="footer-links"><a href="#">Home</a><a href="#">About</a><a href="#">Services</a><a href="#">Contact</a></nav>
</footer>
</body>
</html>
```